依頼詳細
8月の19日に宮城県南三陸町の、つばさ交流センターというところで公演を予定しています。
公演に際して、町民の方々に配布するチラシの作成を依頼させて頂きたいです。

ターゲットは、未就学児くらいの子供とその親や、高齢者の方を想定しています。

当日は公演本編の他に、お客様と出演者の交流会(お茶っこ)や、
子供たちと遊ぶ時間も設ける予定です。

明るくポップで、楽しいごきげんなイメージが伝わるようなデザインを希望します。
記載項目
【表面】

■タイトル

■場所

■入場料

■問い合わせ

■主催/協力

【裏面】

■あらすじ

■キャスト

■スタッフ

■団体紹介

サイズ
A4
ページ数
両面
希望イメージ
シンプル 複雑
単色 カラフル
暗い 明るい
日常 高級
遊び心 厳粛
未来的 伝統的
女性的 男性的
希望する色
黄・オレンジ系、ロゴマークとも調和がとれると嬉しいです。
納品ファイル
• 高解像度JPG (.jpg)
• イラストレーター形式 (.ai)
• PNG形式 (.png)
補足説明
・PDFファイルでも納品いただきたいです。
・裏面のキャストは顔写真を入れていただきたいです。データは後程お渡しします。
・7月3日までに最終データを受け取れるととても助かります!
■ 選んだ理由

民話の内容に沿ったオリジナルのイラストと、お茶っこやモロッパなど細かいところにも
こだわりをもって丁寧に作ってくださっている印象で、メンバー内で一番人気で選ばせていただきました!

■ 提案者全員のお礼・コメント

民話の内容に興味をもって作ってくださったり、お子さんやお年寄りにも見やすいように。と
工夫をしてくださったりして、どれも思いが伝わってきて嬉しくなりました!
これまでは自分たちでチラシの作成もしていたので、プロフェッショナルの手にかかると
こんな風に世界が広がるんだなと、とてもクリエイティブな部分でも刺激を受けました。
ありがとうございました!!

```html
<!DOCTYPE html>
<html lang="ja">
<head>
<meta charset="utf-8">
<title>ばば山 公演チラシ 裏面</title>
<link rel="stylesheet" href="https://fonts.googleapis.com/css2?family=M+PLUS+Rounded+1c:wght@400;700;800&family=Zen+Maru+Gothic:wght@500;700&display=swap">
<style>
  :root {
    --ink: #141414;
    --paper: #ffffff;
    --yellow: #ffd61c;
    --orange: #f5a21a;
    --red: #e8382b;
    --photo: #8c8c8c;
    --logo-tone: #f3c23b;
  }
  * { margin: 0; padding: 0; box-sizing: border-box; }
  html, body { width: 857px; height: 1200px; overflow: hidden; background: var(--paper); }
  .flyer {
    position: relative; width: 857px; height: 1200px; overflow: hidden;
    background: var(--paper); color: var(--ink);
    font-family: "Zen Maru Gothic", "M PLUS Rounded 1c", sans-serif;
  }
  .backdrop { position: absolute; inset: 0; }

  .synopsis {
    position: absolute; left: 72px; top: 60px; width: 726px; height: 320px;
    background: var(--ink); color: var(--paper);
    padding: 60px 16px 0; text-align: center;
  }
  .synopsis-tab {
    position: absolute; left: 50%; top: -14px; transform: translateX(-50%);
    background: var(--red); color: var(--paper);
    font-family: "M PLUS Rounded 1c", sans-serif; font-weight: 800;
    font-size: 22px; letter-spacing: 4px; padding: 8px 34px;
  }
  .synopsis p {
    font-size: 16.5px; font-weight: 700; line-height: 33px;
    letter-spacing: 0; white-space: nowrap;
  }
  .synopsis .accent { color: var(--yellow); }

  .section-head { position: absolute; top: 398px; font-family: "M PLUS Rounded 1c", sans-serif; }
  .section-head .en { font-size: 30px; font-weight: 800; letter-spacing: 1px; line-height: 1; display: block; }
  .section-head .ja { font-size: 10px; font-weight: 700; display: block; margin-top: 1px; letter-spacing: 2px; }
  .section-head .rule { position: absolute; left: 0; top: 46px; height: 3px; background: var(--ink); }
  .cast-head { left: 56px; }
  .cast-head .rule { width: 500px; }
  .staff-head { left: 626px; }
  .staff-head .rule { width: 175px; }

  .member { position: absolute; width: 140px; text-align: center; }
  .member .photo {
    width: 112px; height: 112px; border-radius: 50%; background: var(--photo);
    margin: 0 auto 14px;
  }
  .member .name { font-size: 16px; font-weight: 700; letter-spacing: 1px; }

  .troupe-card {
    position: absolute; left: 28px; top: 820px; width: 188px; height: 355px;
    background: var(--paper); border: 3px solid var(--ink); border-radius: 18px;
    padding: 18px 14px; font-family: "M PLUS Rounded 1c", sans-serif;
  }
  .troupe-card h2 { font-size: 23px; font-weight: 800; line-height: 1.3; }
  .troupe-logo {
    margin-top: 26px; width: 150px; height: 170px; border-radius: 12px;
    background: linear-gradient(160deg, var(--logo-tone), var(--orange));
    display: flex; align-items: flex-end; justify-content: center; padding-bottom: 12px;
    font-size: 17px; font-weight: 800; color: var(--ink);
  }
  .troupe-text {
    position: absolute; left: 240px; top: 868px; width: 596px;
    font-size: 15px; font-weight: 700; line-height: 31px;
  }
</style>
</head>
<body>
<main class="flyer">
  <svg class="backdrop" width="857" height="1200" viewBox="0 0 857 1200" aria-hidden="true">
    <path d="M0 0 H150 C120 60 60 90 0 120 Z" fill="var(--yellow)"/>
    <path d="M857 0 V200 C800 170 760 90 700 0 Z" fill="var(--yellow)"/>
    <path d="M0 330 C90 300 140 380 120 440 C100 520 10 520 0 560 Z" fill="var(--orange)"/>
    <path d="M0 600 C200 520 420 640 600 560 C720 505 800 470 857 440 V1200 H0 Z" fill="var(--yellow)"/>
    <path d="M857 860 C780 900 760 1000 857 1040 Z" fill="var(--orange)"/>
    <path d="M0 760 C60 740 90 800 60 840 C40 870 10 860 0 880 Z" fill="var(--red)"/>
    <circle cx="830" cy="420" r="14" fill="var(--red)"/>
    <circle cx="40" cy="300" r="10" fill="var(--red)"/>
  </svg>

  <section class="synopsis">
    <h2 class="synopsis-tab">あらすじ</h2>
    <p>養蚕農家の姑<span class="accent">おまつ</span>は、息子の嫁である<span class="accent">おたき</span>から、考えが古いとバカにされる毎日。</p>
    <p>ある日、家族で一人だけ浄瑠璃を観に行けなかったおまつ。</p>
    <p>しかし突然、飼い猫の<span class="accent">ミケ</span>が浄瑠璃を語ってみると言い出した。</p>
    <p>「そのかわりオラが語ったと誰かにバラしたら噛みころす」と言うミケ。</p>
    <p>おまつはミケとの約束を守りながら、嫌味な嫁おたきを言い負かす。</p>
    <p>しかしミケは意外なことを言い出して……？</p>
    <p>民話<span class="accent">「ばば山」</span>を原作とした、家族愛がテーマのハッピーエンド物語！</p>
  </section>

  <header class="section-head cast-head"><span class="en">CAST</span><span class="ja">キャスト</span><span class="rule"></span></header>
  <header class="section-head staff-head"><span class="en">STAFF</span><span class="ja">スタッフ</span><span class="rule"></span></header>

  <div class="member" style="left:38px;top:470px"><div class="photo" role="img" aria-label="出演者の顔写真"></div><p class="name">森川陽介</p></div>
  <div class="member" style="left:192px;top:470px"><div class="photo" role="img" aria-label="出演者の顔写真"></div><p class="name">ポポミ</p></div>
  <div class="member" style="left:346px;top:470px"><div class="photo" role="img" aria-label="出演者の顔写真"></div><p class="name">高瀬菜月</p></div>
  <div class="member" style="left:38px;top:640px"><div class="photo" role="img" aria-label="出演者の顔写真"></div><p class="name">高瀬美羽</p></div>
  <div class="member" style="left:192px;top:640px"><div class="photo" role="img" aria-label="出演者の顔写真"></div><p class="name">小野寺杏</p></div>
  <div class="member" style="left:346px;top:640px"><div class="photo" role="img" aria-label="出演者の顔写真"></div><p class="name">宮下和恵</p></div>
  <div class="member" style="left:644px;top:470px"><div class="photo" role="img" aria-label="スタッフの顔写真"></div><p class="name">キョウジュ</p></div>
  <div class="member" style="left:644px;top:640px"><div class="photo" role="img" aria-label="スタッフの顔写真"></div><p class="name">川村七海</p></div>

  <aside class="troupe-card">
    <h2>にこにこ一座<br>とは…</h2>
    <div class="troupe-logo" role="img" aria-label="劇団のロゴマーク">にこにこ一座</div>
  </aside>
  <p class="troupe-text">
    2018年1月に東京で旗揚げをした団体。<br>
    ご縁があって宮城県南三陸町に演劇という文化・娯楽を届けたい！という思いで、毎年町内での公演を実施しています。<br>
    来るたびに会いたい人が増えて、今ではすっかり南三陸の大ファンです！<br>
    マルシェや通販で南三陸の特産品の販売を行うなど、南三陸との絆を深めながら活動をしています。<br>
    私たちは最高なエネルギーで皆さまに笑顔をお届けします！
  </p>
</main>
</body>
</html>
```